Building company business card

Design and print business cards for BRENTHOLM PTY LTD.
A residantial homes building company.
Mark Lantern already designed the company Logo.

```html
<!DOCTYPE html>
<html lang="en">
<head>
<meta charset="utf-8">
<title>BRENTHOLM PTY LTD – Business Cards</title>
<link rel="stylesheet" href="https://fonts.googleapis.com/css2?family=Oswald:wght@500;700&family=Arimo:wght@400&display=swap">
<style>
  :root{
    --navy:#232a6a;
    --gold:#c9973a;
    --gold-light:#e2b85c;
    --white:#ffffff;
    --ink:#2b2b2b;
    --backdrop:#d4d4d2;
  }
  *{margin:0;padding:0;box-sizing:border-box}
  html,body{width:1200px;height:801px;overflow:hidden}
  body{
    background:var(--backdrop);
    position:relative;
    font-family:"Arimo",Arial,sans-serif;
  }
  .card{
    position:absolute;
    width:520px;height:298px;
    border-bottom:3px solid var(--gold);
    border-right:3px solid var(--gold);
    box-shadow:0 14px 30px rgba(0,0,0,.18);
  }
  .card--front{left:50px;top:252px;background:var(--white)}
  .card--back{left:630px;top:252px;background:var(--navy)}

  .brand{
    position:absolute;
    display:flex;align-items:center;gap:10px;
    font-family:"Oswald",Arial Narrow,sans-serif;
    font-weight:700;letter-spacing:1px;
  }
  .brand__square{width:16px;height:16px;background:var(--gold)}
  .card--front .brand{left:36px;top:126px;font-size:34px;color:var(--navy)}
  .card--back .brand{left:0;right:0;top:0;bottom:0;justify-content:center;font-size:52px;color:var(--white)}

  .divider{position:absolute;left:262px;top:40px;width:1px;height:218px;background:var(--navy);opacity:.6}

  .details{position:absolute;left:282px;top:40px;color:var(--ink);font-size:12.5px;line-height:1.45}
  .details__name{
    font-family:"Oswald",Arial Narrow,sans-serif;font-weight:700;
    font-size:19px;color:var(--navy);line-height:1.1;letter-spacing:-.2px
  }
  .details__name .nick{color:var(--gold)}
  .details__role{font-size:13px;margin-bottom:12px}
  .details__licence{color:var(--gold)}
  .details__address{margin-bottom:12px}
  .contact{list-style:none}
  .contact li{display:flex;align-items:center;gap:7px}
  .contact svg{width:11px;height:11px;flex:none}
</style>
</head>
<body>

<section class="card card--front" aria-label="Card front">
  <div class="brand"><span class="brand__square"></span>BRENTHOLM</div>
  <div class="divider"></div>
  <div class="details">
    <p class="details__name">DORIAN <span class="nick">(Dee)</span> CASTELL</p>
    <p class="details__role">Director</p>
    <p class="details__licence">CDB-U 48215</p>
    <p class="details__address">PO Box 287<br>Elmwood North Vic 3190</p>
    <ul class="contact">
      <li><svg viewBox="0 0 12 12"><rect x="3" y="1" width="6" height="10" rx="1" fill="none" stroke="#c9973a" stroke-width="1.3"/></svg>0412 555 310</li>
      <li><svg viewBox="0 0 12 12"><path d="M2 2l2-1 1.5 3-1.2 1a6 6 0 0 0 2.7 2.7l1-1.2 3 1.5-1 2C5 10 2 7 2 2z" fill="#c9973a"/></svg>0433 555 842</li>
      <li><svg viewBox="0 0 12 12"><rect x="1" y="2.5" width="10" height="7" fill="#c9973a"/><path d="M1 2.5l5 4 5-4" fill="none" stroke="#fff" stroke-width="1"/></svg>ddc@brentholm-pl.com</li>
      <li><svg viewBox="0 0 12 12"><circle cx="6" cy="6" r="5" fill="#c9973a"/><path d="M1 6h10M6 1c-2.5 3-2.5 7 0 10M6 1c2.5 3 2.5 7 0 10" fill="none" stroke="#fff" stroke-width=".8"/></svg>www.brentholm-pl.com</li>
    </ul>
  </div>
</section>

<section class="card card--back" aria-label="Card back">
  <div class="brand"><span class="brand__square"></span>BRENTHOLM</div>
</section>

</body>
</html>
```